Company Website for Vortel Insight, an open source data analytics company focused on relationship and li

I need a company/brand website for our new startup, Vortel Insight LLC. We are a company focused on using life pattern analysis techniques, looking at relationships and how relationships, attributes, and activity cluster to infer aggregate information about individuals and groups. Our focus is on improving the digital advertising market.

We have a company logo which I will upload shortly.

Target Market(s)

Digital Advertising

Number of Pages Required

3 page

Font styles to use
Sans Serif

Requirements
Must have
• An main page, about us, contact page.
Nice to have
• Vortel Insight relies on state of the art analytics applied to a the digital marketing space. While it is heavy in science, we also understand the art of influence. The website should have a scientific edge but also a flair that illustrates our focus on applying the hard science and analytics to influencing the behavior of people.

```html
<!DOCTYPE html>
<html lang="en">
<head>
<meta charset="utf-8">
<title>Contact — Vortel Insight</title>
<link href="https://fonts.googleapis.com/css2?family=Montserrat:wght@400;500;600;700&display=swap" rel="stylesheet">
<style>
:root{
  --blue:#1f74c4;
  --dark:#252525;
  --darker:#1c1c1c;
  --base:#2a2a2a;
  --white:#ffffff;
  --muted:#8a8a8a;
  --line:#5a5a5a;
  --map:#e6e6e6;
}
*{margin:0;padding:0;box-sizing:border-box}
html,body{width:1200px;height:1158px;overflow:hidden}
body{font-family:'Montserrat',sans-serif;background:var(--dark);color:var(--white);position:relative}
.abs{position:absolute}

.hero{left:0;top:0;width:1200px;height:236px;background:linear-gradient(100deg,#1b1d22 0%,#2b2c31 45%,#4a4a4e 75%,#3a3a3d 100%)}
.brand{left:116px;top:28px;font-size:26px;font-weight:700;color:var(--blue);letter-spacing:-.5px;display:flex;align-items:center;gap:8px}
.brand-dot{width:10px;height:10px;background:var(--blue);border-radius:50%}
.nav{top:37px;left:548px;display:flex;font-size:13px;font-weight:500}
.nav a{color:var(--white);text-decoration:none;position:absolute;white-space:nowrap}
.nav a.active{color:var(--blue);border-bottom:2px solid var(--blue);padding-bottom:3px}
.nav-icon{top:36px;width:19px;height:19px;border-radius:50%;display:flex;align-items:center;justify-content:center}
.page-title{left:112px;top:124px;font-size:30px;font-weight:500;letter-spacing:.5px}

.info{left:0;top:236px;width:1200px;height:276px;background:var(--dark)}
.heading{font-size:15px;font-weight:500;letter-spacing:.2px}
.heading::after{content:"";display:block;width:56px;height:2px;background:var(--line);margin-top:10px}
.heading.blue::after{background:var(--blue)}
.office-item{left:112px;display:flex;gap:16px;font-size:10.5px;font-weight:600;line-height:1.5}
.circle{width:36px;height:36px;border-radius:50%;background:var(--blue);display:flex;align-items:center;justify-content:center;flex:none}
.intro{left:447px;top:318px;width:640px;font-size:10.5px;font-weight:500;line-height:20px}
.intro p+p{margin-top:20px}
.intro .link{color:var(--blue)}

.map{left:0;top:512px;width:1200px;height:382px;background:linear-gradient(135deg,#ececec,#dedede 60%,#e8e8e8)}
.pin{left:557px;top:672px;background:var(--blue);padding:7px 10px;font-size:13px;font-weight:500}
.pin::after{content:"";position:absolute;left:0;bottom:-8px;border-left:8px solid var(--blue);border-bottom:8px solid transparent}

.form{left:779px;top:574px;width:308px;height:320px;background:var(--darker);padding:16px}
.form .heading{font-size:15px}
.field{left:796px;width:273px;border:1px solid #444;font-size:10.5px;font-weight:500;padding:9px 10px;color:var(--white)}
.send{left:779px;top:894px;width:308px;height:39px;background:var(--blue);font-size:15px;font-weight:500;padding:10px 16px;letter-spacing:.3px}

.foot{font-size:10.5px;font-weight:600;line-height:20px}
.foot-title{color:var(--blue);font-size:12px;font-weight:600}
.social{left:112px;top:1037px;display:flex;gap:8px}
.social span{width:29px;height:29px;border-radius:50%;border:1px solid #777}
.subscribe{left:779px;top:1061px;width:144px;height:27px;border:1px solid #777;border-radius:14px;font-size:10px;color:var(--muted);padding:6px 13px}
.base{left:0;top:1112px;width:1200px;height:46px;background:var(--base);border-top:1px solid #333}
</style>
</head>
<body>

<header class="abs hero" role="img" aria-label="Photo of hands typing on a laptop keyboard"></header>
<div class="abs brand"><span class="brand-dot"></span>Vortel Insight</div>
<nav class="abs nav">
  <a style="left:0">Home</a>
  <a style="left:59px">About us</a>
  <a style="left:136px">Our Team</a>
  <a style="left:240px">Testimonials</a>
  <a style="left:361px">Blog</a>
  <a class="active" style="left:410px">Contact</a>
</nav>
<div class="abs nav-icon" style="left:1033px;background:var(--blue)">
  <svg width="10" height="10" viewBox="0 0 10 10"><path d="M0 1h2l1.2 5h5l1-3.6H3" fill="none" stroke="#fff" stroke-width="1.3"/><circle cx="3.8" cy="8.5" r=".9" fill="#fff"/><circle cx="7.6" cy="8.5" r=".9" fill="#fff"/></svg>
</div>
<div class="abs nav-icon" style="left:1059px;background:#3c3c3c">
  <svg width="10" height="10" viewBox="0 0 10 10"><circle cx="4" cy="4" r="3" fill="none" stroke="#fff" stroke-width="1.4"/><path d="M6.2 6.2L9 9" stroke="#fff" stroke-width="1.5"/></svg>
</div>
<h1 class="abs page-title">CONTACT</h1>

<section class="abs info"></section>
<h2 class="abs heading" style="left:113px;top:272px">OUR HEADDING OFFICE</h2>
<div class="abs office-item" style="top:323px">
  <div class="circle"><svg width="14" height="13" viewBox="0 0 14 13"><path d="M7 0L0 6h2v7h4V9h2v4h4V6h2z" fill="#fff"/></svg></div>
  <div style="padding-top:1px;line-height:1.25">Harborline Works LLC 0000 Delmont,<br>Suite 245 Fairview, IL 0000</div>
</div>
<div class="abs office-item" style="top:380px">
  <div class="circle"><svg width="14" height="14" viewBox="0 0 14 14"><circle cx="7" cy="7" r="6" fill="none" stroke="#fff" stroke-width="1.6"/><path d="M1 7h12M7 1c-3 3-3 9 0 12M7 1c3 3 3 9 0 12" fill="none" stroke="#fff" stroke-width="1.2"/></svg></div>
  <div>WEBSITE &amp; ONLINE STORE<br>htpp://www.vortelinsight.com</div>
</div>
<div class="abs office-item" style="top:437px">
  <div class="circle"><svg width="13" height="13" viewBox="0 0 13 13"><path d="M3 0l2 3-1.4 1.5c.8 1.8 2.3 3.3 4.1 4.1L9.2 7l3 2-1 2.6C6 12 1 7 .4 1.8z" fill="#fff"/></svg></div>
  <div>TELEPHONE<br>(000)&nbsp; 123 456789&nbsp; - (000) 123 456789</div>
</div>

<h2 class="abs heading blue" style="left:447px;top:272px">WE’D LOVE TO HEAR FROM YOU</h2>
<div class="abs intro">
  <p>Have questions about how Vortel Signal can help you streamline operations, improve performance and easily monitor the success of each department? Wondering how the integrated dealer management system works, and how it can work for you?</p>
  <p>Give us a call at <span class="link">1-234-567-890</span> or send us a message using the form below and we'll connect you with a dealer management software expert who can answer your questions.</p>
</div>

<section class="abs map" role="img" aria-label="Street map of New York showing the office location"></section>
<div class="abs pin">VORTEL INSIGHT</div>

<form class="abs form"><h2 class="heading">CONTACT FORM</h2></form>
<div class="abs field" style="top:642px;height:28px">Your name</div>
<div class="abs field" style="top:692px;height:28px">Your email</div>
<div class="abs field" style="top:740px;height:130px">Your message</div>
<div class="abs send">SEND MESSAGE</div>

<div class="abs foot" style="left:112px;top:980px">Copyright 2017-18 <span style="color:var(--blue)">Vortel Insight</span></div>
<div class="abs social"><span></span><span></span><span></span><span></span></div>

<div class="abs foot-title" style="left:444px;top:980px">Our location</div>
<div class="abs foot" style="left:444px;top:1008px;line-height:1.15">Harborline Works LLC 0000 Delmont,<br>Suite 245 Fairview, IL 00000</div>
<div class="abs foot" style="left:444px;top:1038px">Phone : +00 1 23456789<br>Email : info@vortelinsight.com</div>

<div class="abs foot-title" style="left:779px;top:980px">Kepp in touch</div>
<div class="abs foot" style="left:779px;top:1002px;width:320px">Lorem ipsum dolor sit amet, consectetur adi sollicitud ante tellus ornare mi, et mollis</div>
<div class="abs subscribe">Your email
  <svg style="position:absolute;right:10px;top:8px" width="11" height="10" viewBox="0 0 11 10"><path d="M0 5h9M5 1l4 4-4 4" fill="none" stroke="#aaa" stroke-width="1.6"/></svg>
</div>

<footer class="abs base">
  <svg style="position:absolute;left:591px;top:17px" width="18" height="11" viewBox="0 0 18 11"><path d="M1 10l8-8 8 8" fill="none" stroke="#fff" stroke-width="2.5"/></svg>
</footer>

</body>
</html>
```